Brave Tindle website (tool sales website)

place to sell tools that are used to install tiles. We have over 100 tools that can be divided into 5-6 categories we plan to sell our tools online

The business purchases tools wholesale and sells them to customers retail via social media and soon by online website

The product consists of tools and the blades that are used mostly to cut and install tiles like floor tile, shower tiles

Target Market(s)

The target market includes individuals in the building trade and those learning the trade. For example trade schools have used this business exclusively for the tools they need.

Industry/Entity Type

Sales

Coding

Coded - Design and coding required

Number of Pages Required

1 page

Requirements
Must have
• Color and imagery complimentary to the attached logo
• We have approximately 100 items for sale now and think a home page and 5 pages with different tool categories might work best. Categories would be Dimond blade cutting; Coring and Drilling; Grinding and polishing; Manual tile cutters; Other.
• Really only need the space on each page to put the items. We can use Dreamweaver to place actual items and finish the site.
Nice to have
• Need to incorporate a cart for purchases
• We envision something like the US retailer Marlowbee's website, just not as complex. Home page with general info and 5 areas to go to 5 pages each with multiple spots for tools to be listed with info. There is a screen shot below as an example of one of the five
• pages

```html
<!DOCTYPE html>
<html lang="en">
<head>
<meta charset="utf-8">
<title>Brave Tindle – Tile Tools</title>
<link href="https://fonts.googleapis.com/css2?family=Roboto:wght@300;400;500;700&display=swap" rel="stylesheet">
<style>
:root{
  --red:#b30000;
  --red-bright:#d10000;
  --ink:#222;
  --muted:#9a9a9a;
  --line:#e2e2e2;
  --panel:#eeeeee;
  --footer:#1b1b1b;
  --footer-bottom:#0f0f0f;
  --green:#2e9e2e;
  --brown:#8a4a22;
}
*{box-sizing:border-box;margin:0;padding:0}
html,body{width:1200px;height:3273px;overflow:hidden}
body{font-family:"Roboto",sans-serif;color:var(--ink);background:#fff;position:relative}
.abs{position:absolute}

/* header */
.brand{left:85px;top:18px;display:flex;align-items:center;gap:12px}
.brand-mark{width:44px;height:44px;border-radius:50%;background:var(--red)}
.brand-name{font-size:24px;font-weight:700;color:var(--red)}
.social{right:88px;top:12px;display:flex;gap:14px}
.social span{width:20px;height:20px;border-radius:50%;border:1.5px solid var(--red)}
.account{left:700px;top:58px;font-size:12px;color:#444;display:flex;align-items:center;gap:10px}
.cart{left:903px;top:58px;font-size:12px;display:flex;align-items:center;gap:8px}
.cart b{color:var(--red);font-weight:500}

.nav{left:0;top:92px;width:1200px;height:46px;background:var(--red)}
.nav-items{display:flex;height:46px}
.nav-items a{color:#fff;font-size:12px;text-decoration:none;height:46px;display:flex;align-items:center;padding-left:48px;width:130px;border-right:1px solid rgba(255,255,255,.45)}
.nav-items a.first{padding-left:85px;width:168px}
.nav-items a.last{border-right:none}
.search{left:950px;top:102px;width:162px;height:26px;border:1.5px solid #fff;border-radius:13px;color:#fff;font-size:10px;padding:6px 14px}

/* hero */
.hero-a{left:0;top:138px;width:493px;height:287px;background:linear-gradient(180deg,#eef0f2 0%,#d6d8da 45%,#8e8f92 75%,#6f7073 100%)}
.hero-b{left:0;top:430px;width:493px;height:280px;background:linear-gradient(135deg,#fbfbfb 0%,#e4e4e4 55%,#8c9496 85%,#c9c9c9 100%)}
.hero-c{left:498px;top:138px;width:702px;height:572px;background:radial-gradient(ellipse at 35% 20%,#f6f6f4 0%,#e0dfdc 18%,transparent 34%),linear-gradient(170deg,#3a3a3a 0%,#6a6a6a 25%,#a3a3a3 55%,#8a8a8a 80%,#6e6e6e 100%)}
.hero-tag{left:85px;top:325px;color:#fff}
.hero-tag small{font-size:17px;display:block;font-weight:500}
.hero-tag strong{font-size:36px;color:var(--red-bright);font-weight:700}
.offer{left:845px;top:485px;color:#111}
.offer .pct{font-size:80px;font-weight:700;color:var(--red-bright);line-height:1}
.offer .pct span{color:#111;font-weight:400;font-size:52px}
.offer .line1{font-size:28px;font-weight:500;margin-top:4px}
.offer .line2{font-size:15px;font-weight:500;margin-top:4px;padding-bottom:3px;border-bottom:2px solid var(--red)}

/* service strip */
.service{top:731px;width:325px;height:70px;background:var(--red);color:#fff;display:flex;align-items:center;padding-left:16px;gap:26px}
.service .ic{width:44px;height:36px;border:1.5px solid #fff;display:flex;align-items:center;justify-content:center}
.service h4{font-size:15px;font-weight:500}
.service p{font-size:12px;font-weight:300;margin-top:3px}

/* sections */
.heading{left:0;width:1200px;text-align:center;font-size:38px;font-weight:400;letter-spacing:.5px}
.heading em{font-style:normal;color:var(--red)}
.sub{left:0;width:1200px;text-align:center;font-size:15px;color:var(--muted);line-height:26px;font-weight:300}
.tabs{left:140px;top:1038px;width:920px;height:40px;border-bottom:1px solid var(--line);display:flex;font-size:11px;color:#333}
.tabs span{flex:1;text-align:center;line-height:40px}
.tabs .on{border:1px solid var(--line);border-bottom:1px solid #fff;background:#fff;margin-bottom:-1px}

.card{width:236px;height:357px;border:1px solid var(--line);background:#fff;text-align:center}
.card .img{position:absolute;left:28px;top:40px;width:180px;height:120px}
.t-black{background:radial-gradient(ellipse 48% 22% at 50% 55%,#2a2a2a 0%,#5a5a5a 55%,rgba(255,255,255,0) 100%),radial-gradient(circle at 45% 42%,#d40000 0 6%,transparent 7%)}
.t-green{background:radial-gradient(ellipse 34% 40% at 50% 50%,#1f7a4a 0%,#2f9a5e 45%,#b8b8b8 75%,rgba(255,255,255,0) 100%)}
.t-rail{background:radial-gradient(ellipse 46% 24% at 50% 55%,#3b3b3b 0%,#8c8c8c 45%,#c9c9c9 70%,rgba(255,255,255,0) 100%),radial-gradient(circle at 38% 52%,#1f7a4a 0 7%,transparent 8%)}
.t-red{background:radial-gradient(ellipse 46% 26% at 50% 50%,#d11a1a 0%,#a80000 35%,#9a9a9a 65%,rgba(255,255,255,0) 100%)}
.t-tile{background:radial-gradient(ellipse 44% 30% at 50% 52%,#e8c89a 0%,#cfcfcf 45%,#6a6a6a 70%,rgba(255,255,255,0) 100%)}
.t-scorer{background:linear-gradient(120deg,rgba(255,255,255,0) 40%,#c40000 44%,#a00000 56%,rgba(255,255,255,0) 60%)}
.badge{position:absolute;right:8px;top:8px;padding:3px 10px;font-size:10px;color:#fff}
.b-new{background:var(--green)}
.b-sale{background:var(--brown)}
.b-red{background:var(--red)}
.card .name{position:absolute;top:190px;left:0;width:100%;font-size:13px;color:#444;line-height:23px}
.card .price{position:absolute;top:257px;left:16px;font-size:13px;color:#333}
.card .stars{position:absolute;top:254px;right:18px;font-size:14px;color:var(--red);letter-spacing:1px}
.card .stars i{font-style:normal;color:#999}
.card .buy{position:absolute;top:291px;left:57px;width:122px;height:30px;border:1px solid #999;border-radius:15px;font-size:11px;line-height:28px}

/* deal */
.deal-img{left:85px;top:1528px;width:515px;height:375px;background:linear-gradient(180deg,#d9d9d9 0%,#bfbfbf 30%,#efefef 42%,#5c3a22 55%,#6b4428 75%,#3e2614 100%)}
.deal{left:600px;top:1528px;width:513px;height:375px;background:var(--panel);text-align:center}
.deal h2{font-size:36px;font-weight:400;margin-top:30px;letter-spacing:1px}
.deal .rule{width:100px;height:2px;background:var(--red);margin:8px auto 0}
.deal p{font-size:13px;color:#666;line-height:20px;margin:16px 40px 0}
.count{display:flex;gap:22px;justify-content:center;margin-top:20px}
.count div{width:95px;height:76px;border:1px solid #ccc;background:#fff;display:flex;flex-direction:column;justify-content:center;font-size:24px}
.count small{font-size:12px;margin-top:4px}
.count .on{background:var(--red);color:#fff;border-color:var(--red)}
.deal .shop{display:inline-block;margin-top:24px;border:1.5px solid var(--red);padding:10px 24px;font-size:13px}

.pager{left:125px;top:2051px;width:950px;height:1px;background:var(--line)}
.arrows{left:1028px;top:2042px;display:flex;gap:4px}
.arrows span{width:19px;height:19px;display:flex;align-items:center;justify-content:center;border:1px solid #ccc}
.arrows .on{background:var(--red);border-color:var(--red)}

/* testimonial */
.quote-panel{left:85px;top:2502px;width:515px;height:374px;background:var(--panel);text-align:center}
.avatar{position:absolute;left:175px;top:50px;width:118px;height:118px;border-radius:50%;background:radial-gradient(circle at 50% 55%,#e2b592 0%,#c98f6a 45%,#5a3a26 80%);border:4px solid #fff}
.quote-panel p{position:absolute;top:210px;left:20px;width:470px;font-size:14px;line-height:26px;color:#444}
.qmark{font-size:120px;color:#dedede;font-family:Georgia,serif;position:absolute;line-height:1}
.dots{position:absolute;top:332px;left:235px;display:flex;gap:6px}
.dots span{width:9px;height:9px;border-radius:50%;background:#fff}
.dots .on{background:var(--red)}
.quote-img{left:600px;top:2502px;width:513px;height:374px;background:linear-gradient(90deg,#cfcfcf 0%,#e8e8e8 15%,#8a6a4e 35%,#6e5440 55%,#a88e76 70%,#dcdcdc 85%,#bdbdbd 100%)}

/* footer */
.footer{left:0;top:2940px;width:1200px;height:280px;background:var(--footer);color:#fff}
.footer-bottom{left:0;top:3220px;width:1200px;height:53px;background:var(--footer-bottom);color:#ccc;font-size:11px;text-align:center;line-height:53px}
.f-brand{left:88px;top:45px;display:flex;align-items:center;gap:10px}
.f-brand .brand-mark{width:40px;height:40px}
.f-brand .brand-name{font-size:18px}
.f-info{left:96px;top:150px;font-size:13px;line-height:18px;color:#eee}
.f-info .row{display:flex;gap:14px;align-items:flex-start;margin-bottom:16px}
.f-col h5{font-size:13px;font-weight:400;margin-bottom:26px}
.f-links li{list-style:none;font-size:12px;margin-bottom:14px;display:flex;gap:14px}
.field{width:205px;height:30px;border:1px solid #bbb;font-size:10px;color:#aaa;padding:8px;margin-bottom:16px}
.submit{width:205px;height:30px;background:var(--red);text-align:center;font-size:14px;line-height:30px}
.news{display:flex}
.news .in{width:190px;height:38px;background:#e0e0e0;color:#555;font-size:11px;padding:12px 8px}
.news .go{width:40px;height:38px;background:var(--red);display:flex;align-items:center;justify-content:center}
.pay{display:grid;grid-template-columns:repeat(4,50px);gap:12px 10px;margin-top:24px}
.pay span{height:27px;background:#f2f2f2;border-radius:3px}
</style>
</head>
<body>

<!-- header -->
<div class="abs brand"><span class="brand-mark"></span><span class="brand-name">Brave Tindle</span></div>
<div class="abs social"><span></span><span></span><span></span><span></span></div>
<div class="abs account">
  <svg width="18" height="14" viewBox="0 0 18 14"><path d="M1 7h10M7 3l4 4-4 4" fill="none" stroke="#b30000" stroke-width="1.6"/><path d="M10 1h7v12h-7" fill="none" stroke="#444" stroke-width="1.4"/></svg>
  <span>LOGIN &nbsp;|&nbsp; REGISTER</span>
</div>
<div class="abs cart">
  <svg width="20" height="16" viewBox="0 0 20 16"><path d="M1 1h3l2 9h10l2-6H5" fill="none" stroke="#b30000" stroke-width="1.6"/><circle cx="8" cy="14" r="1.5" fill="#b30000"/><circle cx="15" cy="14" r="1.5" fill="#b30000"/></svg>
  <span><b>YOUR CART :</b> 0 ITEMS - £0.00</span>
</div>

<nav class="abs nav">
  <div class="nav-items">
    <a href="#" class="first">HOME</a><a href="#">SHOP</a><a href="#">BLOG</a><a href="#">PAGES</a><a href="#" class="last">FEATURES</a>
  </div>
</nav>
<div class="abs search">Search...</div>

<!-- hero -->
<div class="abs hero-a" role="img" aria-label="Bright room with grey wooden floor and a floor lamp"></div>
<div class="abs hero-b" role="img" aria-label="White tiled bathroom with bathtub and drawers"></div>
<div class="abs hero-c" role="img" aria-label="Bathroom with freestanding tub on patterned grey floor tiles"></div>
<div class="abs hero-tag"><small>DISCOUNT ON</small><strong>NEW ARRIVAL</strong></div>
<div class="abs offer">
  <div class="pct">49%<span> OFF</span></div>
  <div class="line1">ON ALL COLLECTION</div>
  <div class="line2">LOREM IPSUM IS SIMPLY DUMMY OF</div>
</div>

<!-- services -->
<div class="abs service" style="left:85px">
  <div class="ic"><svg width="26" height="18" viewBox="0 0 26 18"><path d="M1 2h15v11H1zM16 6h5l4 4v3h-9z" fill="none" stroke="#fff" stroke-width="1.6"/><circle cx="6" cy="15" r="2" fill="#fff"/><circle cx="20" cy="15" r="2" fill="#fff"/></svg></div>
  <div><h4>WORLDWIDE DELIVERY</h4><p>Lorem ipsum dolor sit amet</p></div>
</div>
<div class="abs service" style="left:437px">
  <div class="ic"><svg width="24" height="18" viewBox="0 0 24 18"><path d="M9 2L2 9l7 7V11h13V7H9z" fill="#fff"/></svg></div>
  <div><h4>EASY RETURNS</h4><p>Lorem ipsum dolor sit amet</p></div>
</div>
<div class="abs service" style="left:788px">
  <div class="ic"><svg width="20" height="20" viewBox="0 0 20 20"><path d="M4 2l4 4-2 3c1 2 3 4 5 5l3-2 4 4-3 3C8 19 1 12 1 5z" fill="#fff"/></svg></div>
  <div><h4>HELPLINE +0800 410 228</h4><p>Lorem ipsum dolor sit amet</p></div>
</div>

<!-- featured 1 -->
<h2 class="abs heading" style="top:877px"><em>FEATURED</em> PRODUCT</h2>
<p class="abs sub" style="top:937px">It is a long established fact that a reader will be distracted by the readable content of a page<br>when looking at its layout.</p>
<div class="abs tabs">
  <span>DIMOND BLADE CUTTING</span><span class="on">CORING AND DRILLING</span><span>GRINDING AND POLISHING</span><span>MANUAL TILE CUTTERS</span><span>OTHER</span>
</div>

<div class="abs card" style="left:85px;top:1120px"><span class="badge b-new">New</span><div class="img t-black" role="img" aria-label="Black manual tile cutter"></div><div class="name">IRONCUT®<br>ADULT LIFE JACKETS - HC105</div><div class="price"><s>$10.99</s> / $12.99</div><div class="stars">★★★★<i>☆</i></div><div class="buy">BUY NOW</div></div>
<div class="abs card" style="left:349px;top:1120px"><span class="badge b-sale">-2%</span><div class="img t-green" role="img" aria-label="Green electric tile saw"></div><div class="name">IRONCUT®<br>ADULT LIFE JACKETS - HC105</div><div class="price"><s>$10.99</s> / $12.99</div><div class="stars">★★★★<i>☆</i></div><div class="buy">BUY NOW</div></div>
<div class="abs card" style="left:613px;top:1120px"><div class="img t-rail" role="img" aria-label="Rail tile cutter"></div><div class="name">IRONCUT®<br>ADULT LIFE JACKETS - HC105</div><div class="price"><s>$10.99</s> / $12.99</div><div class="stars">★★★★<i>☆</i></div><div class="buy">BUY NOW</div></div>
<div class="abs card" style="left:877px;top:1120px"><span class="badge b-new">New</span><div class="img t-red" role="img" aria-label="Red manual tile cutter"></div><div class="name">IRONCUT®<br>ADULT LIFE JACKETS - HC105</div><div class="price"><s>$10.99</s> / $12.99</div><div class="stars">★★★★<i>☆</i></div><div class="buy">BUY NOW</div></div>

<!-- deal -->
<div class="abs deal-img" role="img" aria-label="Bedroom with dark wooden floor and white tile inlays"></div>
<div class="abs deal">
  <h2>DEAL OF THE DAY</h2>
  <div class="rule"></div>
  <p>Duis aute irure dolor in reprehenderit in voluptate velit esse cillum dolore eu fugiat nulla pariatur. Excepteur sint occaecat cupidatat non proident, sunt in culpa fugats vitaes nemo minima rerums unsers sadips.</p>
  <div class="count">
    <div class="on">144<small>DAYS</small></div>
    <div>8<small>HRS</small></div>
    <div>16<small>MIN</small></div>
    <div>27<small>SEC</small></div>
  </div>
  <span class="shop">SHOP NOW</span>
</div>

<!-- featured 2 -->
<h2 class="abs heading" style="top:1974px"><em>FEATURED</em> PRODUCT</h2>
<div class="abs pager"></div>
<div class="abs arrows">
  <span><svg width="8" height="10" viewBox="0 0 8 10"><path d="M6 1L2 5l4 4" fill="none" stroke="#666" stroke-width="1.6"/></svg></span>
  <span class="on"><svg width="8" height="10" viewBox="0 0 8 10"><path d="M2 1l4 4-4 4" fill="none" stroke="#fff" stroke-width="1.6"/></svg></span>
</div>

<div class="abs card" style="left:85px;top:2095px"><span class="badge b-red">New</span><div class="img t-tile" role="img" aria-label="Tile cutter with tile"></div><div class="name">IRONCUT®<br>ADULT LIFE JACKETS - HC105</div><div class="price"><s>$10.99</s> / $12.99</div><div class="stars">★★★★<i>☆</i></div><div class="buy">BUY NOW</div></div>
<div class="abs card" style="left:349px;top:2095px"><div class="img t-rail" role="img" aria-label="Tile cutter cutting a tile"></div><div class="name">IRONCUT®<br>ADULT LIFE JACKETS - HC105</div><div class="price"><s>$10.99</s> / $12.99</div><div class="stars">★★★★<i>☆</i></div><div class="buy">BUY NOW</div></div>
<div class="abs card" style="left:613px;top:2095px"><span class="badge b-new">-2%</span><div class="img t-scorer" role="img" aria-label="Red handheld tile scorer"></div><div class="name">IRONCUT®<br>ADULT LIFE JACKETS - HC105</div><div class="price"><s>$10.99</s> / $12.99</div><div class="stars">★★★★<i>☆</i></div><div class="buy">BUY NOW</div></div>
<div class="abs card" style="left:877px;top:2095px"><span class="badge b-sale">New</span><div class="img t-red" role="img" aria-label="Long red tile cutter"></div><div class="name">IRONCUT®<br>ADULT LIFE JACKETS - HC105</div><div class="price"><s>$10.99</s> / $12.99</div><div class="stars">★★★★<i>☆</i></div><div class="buy">BUY NOW</div></div>

<!-- testimonial -->
<div class="abs quote-panel">
  <div class="avatar" role="img" aria-label="Customer portrait"></div>
  <span class="qmark" style="left:14px;top:160px">“</span>
  <span class="qmark" style="right:24px;top:270px">”</span>
  <p>It is a long established fact that a reader will be distracted by the readable content of a page when looking at its layout.The point of using Lorem Ipsum is that it has a more-or-less normal distribution of letters,</p>
  <div class="dots"><span></span><span class="on"></span></div>
</div>
<div class="abs quote-img" role="img" aria-label="Modern kitchen with wood panels and stone floor tiles"></div>

<!-- footer -->
<footer class="abs footer">
  <div class="abs f-brand"><span class="brand-mark"></span><span class="brand-name">Brave Tindle</span></div>
  <div class="abs f-info">
    <div class="row"><svg width="10" height="14" viewBox="0 0 10 14"><path d="M5 0a5 5 0 0 1 5 5c0 4-5 9-5 9S0 9 0 5a5 5 0 0 1 5-5z" fill="#fff"/><circle cx="5" cy="5" r="2" fill="#1b1b1b"/></svg><span>It is a long<br>established fact that<br>a reader will be</span></div>
    <div class="row"><svg width="12" height="12" viewBox="0 0 20 20"><path d="M4 2l4 4-2 3c1 2 3 4 5 5l3-2 4 4-3 3C8 19 1 12 1 5z" fill="#fff"/></svg><span>555-210-0193</span></div>
  </div>
  <div class="abs f-col" style="left:385px;top:50px">
    <h5>Quick Links</h5>
    <ul class="f-links"><li>→<span>home</span></li><li>→<span>shop</span></li><li>→<span>blog</span></li><li>→<span>pages</span></li><li>→<span>features</span></li></ul>
  </div>
  <div class="abs f-col" style="left:563px;top:50px">
    <h5>Contact Us</h5>
    <div class="field">Name..</div><div class="field">Email..</div><div class="field">Phone No..</div><div class="submit">SUBMIT</div>
  </div>
  <div class="abs f-col" style="left:850px;top:50px">
    <h5>Subscribe Newsletter</h5>
    <div class="news"><div class="in">Enter Your Email ID..</div><div class="go"><svg width="16" height="12" viewBox="0 0 16 12"><path d="M1 1h14v10H1zM1 1l7 6 7-6" fill="none" stroke="#fff" stroke-width="1.5"/></svg></div></div>
    <div class="pay"><span></span><span></span><span></span><span></span><span></span><span></span><span></span></div>
  </div>
</footer>
<div class="abs footer-bottom">bravetindle.com2017. All rights reserved</div>

</body>
</html>
```